I own a small business whose primary function is Professional Fashion and Commercial Photography and has a secondary function of Talent Management of Models/Actors. I've used NorthPress in the past to print my own design, but I'd like something a bit more topical, fresh and done by an artist instead of a photographer (me).

My company logo is included with a few selected horizontal (landscape) photos of some of my models--I'd like to use a single model photo as the background for the entire card, either in color or converted to black and white, at opacity enough to see the photo but not too much to obscure any text or the company logo, or use a photo as a share of the card (not the entire background), or use all the three models on the card in some manor... Our company colors are white, black, grey-silver and red.

Industry/Entity Type

Small Business

Contact Information for Business Card

Daniel Hartwell, Owner
KTL Productions
PO Box 7713
Brattleboro VT 05917-7713
(860) 555-0147
dan@ktlproductions-example,.com

```html
<!DOCTYPE html>
<html lang="en">
<head>
<meta charset="UTF-8">
<title>KTL Productions — Business Card</title>
<link rel="stylesheet" href="https://fonts.googleapis.com/css2?family=Cabin:wght@400;600&display=swap">
<style>
  :root {
    --page-bg: #e9e6e2;
    --card-white: #ffffff;
    --card-black: #0b0b0b;
    --photo-dark: #1c1c1c;
    --photo-mid: #2a2a2a;
    --brand-red: #e3262b;
    --ink: #111111;
    --ink-soft: #333333;
  }
  * { box-sizing: border-box; margin: 0; padding: 0; }
  html, body {
    width: 1200px; height: 1000px; overflow: hidden;
    background: var(--page-bg);
    font-family: "Cabin", "Segoe UI", sans-serif;
  }
  .sheet {
    width: 1200px; height: 1000px;
    display: flex; flex-direction: column; align-items: center; justify-content: center;
    gap: 40px;
  }
  .card {
    position: relative;
    width: 780px; height: 446px;
    overflow: hidden;
    box-shadow: 0 6px 18px rgba(0,0,0,0.18);
  }

  /* Back side */
  .card--back { background: var(--card-black); }
  .card-back__photo {
    position: absolute; left: 120px; top: 0; width: 420px; height: 446px;
    background: radial-gradient(ellipse at 45% 40%, var(--photo-mid) 0%, var(--photo-dark) 45%, var(--card-black) 80%);
    opacity: 0.9;
  }
  .card-back__brand {
    position: absolute; left: 190px; top: 188px;
    display: flex; align-items: center; gap: 18px;
    color: var(--card-white);
  }
  .brand-square {
    width: 58px; height: 58px;
    border: 4px solid currentColor;
  }
  .card-back__brand .brand-name {
    font-size: 44px; font-weight: 600; letter-spacing: 3px;
  }

  /* Front side */
  .card--front { background: var(--card-white); }
  .card-front__brand {
    position: absolute; right: 56px; top: 46px;
    display: flex; align-items: center; gap: 12px;
    color: var(--ink);
  }
  .card-front__brand .brand-square {
    width: 34px; height: 34px; border: none; background: var(--brand-red);
  }
  .card-front__brand .brand-name {
    font-size: 28px; font-weight: 600; letter-spacing: 2px;
  }
  .holder {
    position: absolute; left: 150px; top: 140px;
  }
  .holder__name {
    font-size: 31px; font-weight: 400; color: var(--brand-red); line-height: 1.1;
  }
  .holder__role {
    font-size: 19px; color: var(--ink-soft); margin-top: 4px; margin-left: -10px;
  }
  .contacts {
    position: absolute; left: 118px; top: 232px;
    list-style: none;
    font-size: 21px; color: var(--ink);
  }
  .contacts li {
    display: flex; align-items: center; gap: 10px;
    height: 36px; white-space: nowrap;
  }
  .contacts svg { width: 20px; height: 20px; fill: var(--ink); flex: none; }
  .contacts .indent-1 { padding-left: 30px; }
  .contacts .indent-2 { padding-left: 20px; }
  .contacts .indent-3 { padding-left: 10px; }
</style>
</head>
<body>
  <main class="sheet">
    <section class="card card--back" aria-label="Card back">
      <div class="card-back__photo" role="img" aria-label="Faint black and white portrait of a model in a cap, set into the dark background"></div>
      <div class="card-back__brand">
        <span class="brand-square"></span>
        <span class="brand-name">KTL Productions</span>
      </div>
    </section>

    <section class="card card--front" aria-label="Card front">
      <div class="card-front__brand">
        <span class="brand-square"></span>
        <span class="brand-name">KTL Productions</span>
      </div>

      <div class="holder">
        <p class="holder__name">Daniel Hartwell</p>
        <p class="holder__role">Owner</p>
      </div>

      <ul class="contacts">
        <li class="indent-1">
          <svg viewBox="0 0 24 24" aria-hidden="true"><path d="M12 3 2 12h3v9h5v-6h4v6h5v-9h3z"/></svg>
          PO BOX 7713 Harlow Ridge ME
        </li>
        <li class="indent-2">
          <svg viewBox="0 0 24 24" aria-hidden="true"><path d="M6.6 10.8a15.1 15.1 0 0 0 6.6 6.6l2.2-2.2a1 1 0 0 1 1-.25 11.4 11.4 0 0 0 3.6.57 1 1 0 0 1 1 1V20a1 1 0 0 1-1 1A17 17 0 0 1 3 4a1 1 0 0 1 1-1h3.5a1 1 0 0 1 1 1c0 1.25.2 2.45.57 3.57a1 1 0 0 1-.25 1z"/></svg>
          04917 7713
        </li>
        <li class="indent-3">
          <svg viewBox="0 0 24 24" aria-hidden="true"><path d="M7 1h10a2 2 0 0 1 2 2v18a2 2 0 0 1-2 2H7a2 2 0 0 1-2-2V3a2 2 0 0 1 2-2zm0 3v15h10V4zm4 16.2a1 1 0 1 0 2 0 1 1 0 0 0-2 0z"/></svg>
          (555) 555 0147
        </li>
        <li>
          <svg viewBox="0 0 24 24" aria-hidden="true"><path d="M2 5h20v14H2zm2 2v.4l8 5.3 8-5.3V7zm16 2.8-8 5.3-8-5.3V17h16z"/></svg>
          dan@ktlproductions-example.com
        </li>
      </ul>
    </section>
  </main>
</body>
</html>
```